Brill's Jewelers website (www.brillsjewelers-example.com)

We are in need of a web storefront for a retail Jewelry store.
www.brillsjewelers-example.com
https://www.facebook.com/Brills-Jewelers-Palm-Vista-740315928461257/

Brill's Jewelers is located in Coral Gables, Florida. The store has been family owned and operated since 1958. Their focus customers are high-income families that care about quality over the brand name. They mostly sell fashion jewelry and diamonds up to 8 carats. We are looking for a simple minimalistic site that their customers can view their inventory and purchase items online.

Competitors websites:
https://www.orvinjewelers-example.com/
http://www.pelvaro-example.com/
http://truecutjewelers-example.com/

Pages:
-Home (with message bulletin)
-Jewelry
We would be able to create the subpages ie Rings, Bracelets, Earrings, Necklaces, Estate, Watches, Men's, Children's
-Services
We would need sub pages ie Appraisals, Consignment, Repairs
-About us
-Contact

Target Market(s)

Local wealthy families

Coding

Number of Pages Required

Font styles to use
Serif

Requirements
Must have
• -An E-commerce site customers can buy jewelry online.
-An easy process internally to add new items to the site
-Colors are Black and White or Black and Gold
Nice to have
• I would like to stay away from face shots of random models in stock photos. I want the jewelry pieces as the focus, not models.

```html
<!DOCTYPE html>
<html lang="en">
<head>
<meta charset="utf-8">
<title>Brill's Jewelers — Your Hometown Jeweler</title>
<link href="https://fonts.googleapis.com/css2?family=Lato:wght@400;700;900&display=swap" rel="stylesheet">
<style>
:root{
  --gold:#c08a2b;
  --ink:#111111;
  --text:#333333;
  --muted:#666666;
  --rule:#cfcfcf;
  --bar:#f2f2f2;
  --tile:#efefef;
  --white:#ffffff;
}
*{box-sizing:border-box;margin:0;padding:0}
html,body{width:1200px;height:2754px;overflow:hidden}
body{position:relative;background:var(--white);font-family:'Lato',sans-serif;color:var(--text)}
.abs{position:absolute}
.topbar{left:0;top:0;width:1200px;height:50px;background:var(--bar)}
.social{display:flex;gap:9px}
.social span{width:25px;height:25px;border:1.5px solid #555;border-radius:50%;display:flex;align-items:center;justify-content:center}
.social svg{width:11px;height:11px;fill:#555}
.topbar .social{left:75px;top:13px}
.top-icons{right:149px;top:17px;display:flex;gap:30px}
.top-icons svg{width:14px;height:14px;fill:#444}
.header{left:0;top:50px;width:1200px;height:102px}
.brand{left:75px;top:37px;display:flex;align-items:center;gap:12px}
.brand-mark{width:14px;height:14px;background:var(--gold)}
.brand-name{font-weight:900;font-size:28px;line-height:28px;color:var(--ink);letter-spacing:.5px}
.nav{right:75px;top:38px;display:flex;align-items:center;font-weight:700;font-size:14px;color:var(--ink)}
.nav a{margin-left:39px;text-decoration:none;color:inherit;padding-bottom:10px;border-bottom:2px solid transparent}
.nav a.active{color:var(--gold);border-color:var(--gold);padding:0 10px 10px;margin-left:0}
.cart{display:flex;align-items:center;margin-left:34px;padding-bottom:10px;color:#777;font-weight:400}
.cart i{width:34px;height:34px;border:1.5px solid #444;border-radius:50%;display:flex;align-items:center;justify-content:center;margin-right:13px}
.cart svg{width:14px;height:14px;fill:#222}
.cart b{color:var(--gold)}
.hero{left:0;top:152px;width:1200px;height:606px;background:radial-gradient(ellipse at 60% 45%,#fafafa 0%,#eeeeee 70%,#e8e8e8 100%)}
.hero-visual{left:560px;top:80px;width:520px;height:430px;background:radial-gradient(ellipse at 50% 50%,#ffffff 0%,#d6d6d6 40%,#c4c4c4 55%,rgba(235,235,235,0) 70%)}
.hero-title{left:75px;top:212px;font-weight:900;font-size:56px;color:var(--ink);letter-spacing:1px}
.hero-sub{left:75px;top:286px;font-weight:700;font-size:27px;color:var(--ink)}
.btn{display:flex;align-items:center;justify-content:center;background:var(--gold);color:var(--white);font-weight:700;font-size:15px;text-decoration:none}
.hero .btn{left:75px;top:338px;width:153px;height:45px}
.dots{left:565px;top:546px;display:flex;gap:8px}
.dots i{width:11px;height:11px;border-radius:50%;background:#444}
.dots i:first-child{background:var(--gold)}
.section-title{left:317px;width:568px;display:flex;align-items:center;gap:52px;font-weight:900;font-size:27px;color:var(--ink);white-space:nowrap}
.section-title::before,.section-title::after{content:"";flex:1;height:1px;background:var(--rule)}
.arrow{width:16px;height:26px;fill:none;stroke:#444;stroke-width:1.6}
.category{top:883px;width:252px;height:318px;background:var(--tile)}
.category-visual{left:30px;top:30px;width:192px;height:190px;border-radius:50%;background:radial-gradient(circle,#ffffff 0%,#dcdcdc 55%,rgba(239,239,239,0) 72%)}
.category-label{left:18px;top:254px;width:216px;height:44px;background:var(--white);display:flex;align-items:center;justify-content:center;font-weight:900;font-size:14px;color:var(--ink)}
.view-all{left:492px;top:1250px;width:216px;height:44px}
.divider{left:75px;top:1346px;width:1051px;height:1px;background:var(--rule)}
.product{top:1463px;width:242px}
.product-visual{width:242px;height:200px;background:radial-gradient(circle at 50% 50%,#ffffff 0%,#ececec 75%)}
.product-head{margin-top:20px;display:flex;justify-content:space-between;font-weight:700;font-size:15px;color:var(--ink)}
.product-head svg{width:14px;height:14px;fill:#888;margin-right:22px}
.product-price{margin-top:5px;display:flex;justify-content:space-between;font-weight:700;font-size:15px;color:var(--gold)}
.product-price svg{width:16px;height:14px;fill:#888;margin-right:21px}
.add-cart{margin-top:11px;width:131px;height:39px;background:var(--ink);color:var(--white);display:flex;align-items:center;justify-content:center;gap:8px;font-weight:700;font-size:13.5px}
.add-cart svg{width:12px;height:12px;fill:var(--white)}
.welcome{left:0;top:1851px;width:1200px;height:380px;background:#000}
.store-visual{left:0;top:0;width:586px;height:380px;background:linear-gradient(160deg,#9c8f86 0%,#6e655f 45%,#2a2422 60%,#b8a58a 100%)}
.welcome h2{left:627px;top:57px;color:var(--white);font-weight:900;font-size:27px}
.welcome p{left:629px;top:112px;width:490px;color:#e6e6e6;font-size:15px;line-height:26.8px}
.welcome .btn{left:629px;top:271px;width:152px;height:45px}
.newsletter-sub{left:0;top:2341px;width:1200px;text-align:center;font-size:15px;color:var(--text)}
.email{left:317px;top:2383px;width:449px;height:43px;border:1px solid #bbb;font-size:13px;color:#333;display:flex;align-items:center;padding-left:15px}
.signup{left:780px;top:2383px;width:104px;height:43px}
.footer{left:0;top:2497px;width:1200px;height:257px;background:#f0f0f0}
.fcol{top:52px}
.fcol h4{font-weight:700;font-size:15px;color:var(--ink);margin-bottom:10px}
.fcol li{list-style:none;font-size:13px;color:#333;line-height:28.5px}
.contact-line{display:flex;align-items:center;gap:20px}
.contact-line svg{width:12px;height:12px;fill:#333}
.footer .social{margin-top:13px;gap:8px}
.footer .social span{width:32px;height:32px}
.copy{margin-top:24px;font-size:13px;line-height:21px;color:#333}
</style>
</head>
<body>

<div class="abs topbar">
  <div class="abs social">
    <span><svg viewBox="0 0 10 10"><rect x="4" y="1" width="2" height="8"/><rect x="3" y="4" width="4" height="1.5"/></svg></span>
    <span><svg viewBox="0 0 10 10"><circle cx="5" cy="5" r="3" fill="none" stroke="#555" stroke-width="1.4"/></svg></span>
    <span><svg viewBox="0 0 10 10"><path d="M1 7 Q5 9 9 2 Q6 4 4 3 Q2 5 1 7z"/></svg></span>
    <span><svg viewBox="0 0 10 10"><rect x="1.5" y="1.5" width="7" height="7" rx="2" fill="none" stroke="#555" stroke-width="1.2"/><circle cx="5" cy="5" r="1.6" fill="none" stroke="#555" stroke-width="1.2"/></svg></span>
  </div>
  <div class="abs top-icons">
    <svg viewBox="0 0 14 14"><circle cx="7" cy="4" r="3"/><path d="M1 14 Q1 8 7 8 Q13 8 13 14z"/></svg>
    <svg viewBox="0 0 14 14"><circle cx="6" cy="6" r="4.2" fill="none" stroke="#444" stroke-width="2"/><path d="M9 9l4 4" stroke="#444" stroke-width="2.4"/></svg>
  </div>
</div>

<header class="abs header">
  <div class="abs brand">
    <span class="brand-mark"></span>
    <span class="brand-name">BRILL'S JEWELERS</span>
  </div>
  <nav class="abs nav">
    <a class="active" href="#">HOME</a>
    <a href="#">JEWELRY</a>
    <a href="#">SERVICES</a>
    <a href="#">ABOUT US</a>
    <a href="#">CONTACT</a>
    <span class="cart"><i><svg viewBox="0 0 14 14"><path d="M0 2h3l2 7h7l2-5H4.5" fill="none" stroke="#222" stroke-width="1.6"/><circle cx="6" cy="12" r="1.3"/><circle cx="11" cy="12" r="1.3"/></svg></i>MY CART&nbsp;<b>(0)</b></span>
  </nav>
</header>

<section class="abs hero">
  <div class="abs hero-visual" role="img" aria-label="Diamond halo engagement ring in white gold"></div>
  <h1 class="abs hero-title">BRILL'S</h1>
  <div class="abs hero-sub">YOUR HOMETOWN JEWELER</div>
  <a class="abs btn" href="#">SHOP NOW</a>
  <div class="abs dots"><i></i><i></i><i></i><i></i></div>
</section>

<h2 class="abs section-title" style="top:813px">JEWELRY</h2>
<svg class="abs arrow" style="left:38px;top:1030px" viewBox="0 0 16 26"><path d="M13 2L3 13l10 11"/></svg>
<svg class="abs arrow" style="left:1150px;top:1030px" viewBox="0 0 16 26"><path d="M3 2l10 11L3 24"/></svg>

<div class="abs category" style="left:75px"><div class="abs category-visual" role="img" aria-label="Pearl and diamond stud earrings"></div><div class="abs category-label">SHOP RINGS</div></div>
<div class="abs category" style="left:340px"><div class="abs category-visual" role="img" aria-label="Gold pendant with round diamond"></div><div class="abs category-label">SHOP NECKLACES</div></div>
<div class="abs category" style="left:608px"><div class="abs category-visual" role="img" aria-label="Diamond stud earrings"></div><div class="abs category-label">SHOP EARRINGS</div></div>
<div class="abs category" style="left:874px"><div class="abs category-visual" role="img" aria-label="Silver and gold beaded bracelets"></div><div class="abs category-label">SHOP BRACELETS</div></div>

<a class="abs btn view-all" href="#">VIEW ALL COLLECTIONS</a>
<div class="abs divider"></div>

<h2 class="abs section-title" style="top:1392px">FEATURED PRODUCTS</h2>
<svg class="abs arrow" style="left:38px;top:1619px" viewBox="0 0 16 26"><path d="M13 2L3 13l10 11"/></svg>
<svg class="abs arrow" style="left:1150px;top:1619px" viewBox="0 0 16 26"><path d="M3 2l10 11L3 24"/></svg>

<div class="abs product" style="left:75px">
  <div class="product-visual" role="img" aria-label="Diamond halo engagement ring"></div>
  <div class="product-head">PRODUCT HEADING<svg viewBox="0 0 14 14"><circle cx="7" cy="7" r="7"/><rect x="6" y="6" width="2" height="5" fill="#fff"/><circle cx="7" cy="4" r="1.1" fill="#fff"/></svg></div>
  <div class="product-price">$10.00<svg viewBox="0 0 16 14"><path d="M8 14L1.5 7.5A4 4 0 0 1 8 2.5A4 4 0 0 1 14.5 7.5z"/></svg></div>
  <div class="add-cart"><svg viewBox="0 0 12 12"><path d="M0 1h2.5l1.5 6h6.5l1.5-4.5H3.2z"/><circle cx="5" cy="10.5" r="1.2"/><circle cx="9.5" cy="10.5" r="1.2"/></svg>ADD TO CART</div>
</div>
<div class="abs product" style="left:343px">
  <div class="product-visual" role="img" aria-label="Diamond hoop earrings"></div>
  <div class="product-head">PRODUCT HEADING<svg viewBox="0 0 14 14"><circle cx="7" cy="7" r="7"/><rect x="6" y="6" width="2" height="5" fill="#fff"/><circle cx="7" cy="4" r="1.1" fill="#fff"/></svg></div>
  <div class="product-price">$10.00<svg viewBox="0 0 16 14"><path d="M8 14L1.5 7.5A4 4 0 0 1 8 2.5A4 4 0 0 1 14.5 7.5z"/></svg></div>
  <div class="add-cart"><svg viewBox="0 0 12 12"><path d="M0 1h2.5l1.5 6h6.5l1.5-4.5H3.2z"/><circle cx="5" cy="10.5" r="1.2"/><circle cx="9.5" cy="10.5" r="1.2"/></svg>ADD TO CART</div>
</div>
<div class="abs product" style="left:615px">
  <div class="product-visual" role="img" aria-label="Pearl stud earrings with diamond accents"></div>
  <div class="product-head">PRODUCT HEADING<svg viewBox="0 0 14 14"><circle cx="7" cy="7" r="7"/><rect x="6" y="6" width="2" height="5" fill="#fff"/><circle cx="7" cy="4" r="1.1" fill="#fff"/></svg></div>
  <div class="product-price">$10.00<svg viewBox="0 0 16 14"><path d="M8 14L1.5 7.5A4 4 0 0 1 8 2.5A4 4 0 0 1 14.5 7.5z"/></svg></div>
  <div class="add-cart"><svg viewBox="0 0 12 12"><path d="M0 1h2.5l1.5 6h6.5l1.5-4.5H3.2z"/><circle cx="5" cy="10.5" r="1.2"/><circle cx="9.5" cy="10.5" r="1.2"/></svg>ADD TO CART</div>
</div>
<div class="abs product" style="left:883px">
  <div class="product-visual" role="img" aria-label="Diamond clover drop earrings"></div>
  <div class="product-head">PRODUCT HEADING<svg viewBox="0 0 14 14"><circle cx="7" cy="7" r="7"/><rect x="6" y="6" width="2" height="5" fill="#fff"/><circle cx="7" cy="4" r="1.1" fill="#fff"/></svg></div>
  <div class="product-price">$10.00<svg viewBox="0 0 16 14"><path d="M8 14L1.5 7.5A4 4 0 0 1 8 2.5A4 4 0 0 1 14.5 7.5z"/></svg></div>
  <div class="add-cart"><svg viewBox="0 0 12 12"><path d="M0 1h2.5l1.5 6h6.5l1.5-4.5H3.2z"/><circle cx="5" cy="10.5" r="1.2"/><circle cx="9.5" cy="10.5" r="1.2"/></svg>ADD TO CART</div>
</div>

<section class="abs welcome">
  <div class="abs store-visual" role="img" aria-label="Store interior with glass jewelry display cases"></div>
  <h2 class="abs">WELCOME TO OUR WEBSITE</h2>
  <p class="abs">Aliquam molestie, mi et imperdiet euismod, dui purus auctor tellus, et interdum lacus lectus et ante. Sed accumsan sollicitudin sapien, sit amet adipiscing turpis gravida ac. In congue, neque ac lobortis volutpat, libero mauris varius mi, vitae suscipit ipsum ligula vitae risusaliquam nibh a dui iaculis viverra id a velit.</p>
  <a class="abs btn" href="#">READ MORE</a>
</section>

<h2 class="abs section-title" style="top:2292px">EMAIL NEWSLETTER</h2>
<div class="abs newsletter-sub">By signing up you agree to receive promotional emails</div>
<div class="abs email">Email Address</div>
<a class="abs btn signup" href="#">SIGN UP</a>

<footer class="abs footer">
  <div class="abs fcol" style="left:75px">
    <h4>SITE MAP</h4>
    <ul><li>Home</li><li>Jewelry</li><li>Services</li><li>About us</li><li>Contact</li></ul>
  </div>
  <div class="abs fcol" style="left:301px">
    <h4>MY ACCOUNT</h4>
    <ul><li>My Orders</li><li>Create Account</li><li>Refer Friends</li><li>Returns &amp; Exchanges</li></ul>
  </div>
  <div class="abs fcol" style="left:564px">
    <h4>CONTACT INFO</h4>
    <ul>
      <li style="line-height:21px;padding-top:3px">412 Alder Lane<br>Palm Vista, FL 33100</li>
      <li class="contact-line"><svg viewBox="0 0 12 12"><path d="M2 0l3 3-1.5 1.5a7 7 0 0 0 4 4L9 7l3 3-2 2C4 12 0 8 0 2z"/></svg>1-800-555-0142</li>
      <li class="contact-line"><svg viewBox="0 0 12 12"><rect y="2" width="12" height="8"/><path d="M0 2l6 5 6-5" stroke="#f0f0f0" fill="none"/></svg>info@brillsjewelers-example.com</li>
    </ul>
  </div>
  <div class="abs fcol" style="left:857px">
    <h4>FOLLOW US</h4>
    <div class="social">
      <span><svg viewBox="0 0 10 10"><rect x="4" y="1" width="2" height="8"/><rect x="3" y="4" width="4" height="1.5"/></svg></span>
      <span><svg viewBox="0 0 10 10"><circle cx="5" cy="5" r="3" fill="none" stroke="#555" stroke-width="1.4"/></svg></span>
      <span><svg viewBox="0 0 10 10"><path d="M1 7 Q5 9 9 2 Q6 4 4 3 Q2 5 1 7z"/></svg></span>
      <span><svg viewBox="0 0 10 10"><rect x="1.5" y="1.5" width="7" height="7" rx="2" fill="none" stroke="#555" stroke-width="1.2"/><circle cx="5" cy="5" r="1.6" fill="none" stroke="#555" stroke-width="1.2"/></svg></span>
    </div>
    <div class="copy">Copyright © 2020. Company Name<br>All Right Reserved</div>
  </div>
</footer>

</body>
</html>
```